Business Card Design for a Private Label Pet Company

We need a business card design for our family-owned company, Hollow Creek Pet Works (www.hollowcreekpetworks.com), out of St. Louis, MO. We provide turnkey private label solutions for retailers, Marketvale sellers and other brands who want to provide high quality, natural, Made in the USA pet products to their customers. Our customer are worldwide and range from the US to the UK to Vietnam and beyond. We offer private label for dozens of pet products including grooming products (shampoos, conditioners, colognes, ear and eye washes, mouthwash, etc.), all meat treats, supplements, and specialty products (pet stain and odor cleaner, anti-chew spray, etc.). We would like to see designs that use the colors, fonts and logos (see variations) within our brand guidelines and fit with the look and feel from our website.

Target Market(s)

Pet Store Owners, Marketvale Sellers, Pet Brand Marketers

Industry/Entity Type

Pet

Contact Information for Business Card

Tom Willoughby
CEO
Hollow Creek Pet Works
5817 Brookhaven Commerce Lane
St. Louis, MO 63521
office: 314.555.0182
mobile: 770.555.0139
email: tom@hollowcreekpetworks.com

Colors

Designer to choose colors to be used in the design.

Requirements
Must have
• Need to follow the brand guidelines attached for colors, fonts and logos
• Need to use the logos attached (or a variation) with our without the tagline
• Name, title, phone (office and mobil), email, address on the business card
• Clean professional look and feel that says: high quality natural pet products, high quality service, made in the USA
Nice to have
• Made in the USA is a big positive in our industry and we are very proud of it. There is an attached icon from our website. The designer can get creative here as they wish.
• I do like using color for pop. Just don't like lots of bright, loud colors.
Should not have
• lots of bright, loud colors
• overwhelming to the reader
• crowded

```html
<!DOCTYPE html>
<html lang="en">
<head>
<meta charset="utf-8">
<title>Hollow Creek Pet Works — Business Card</title>
<link rel="stylesheet" href="https://fonts.googleapis.com/css2?family=Merriweather:wght@400;700;900&display=swap">
<style>
  :root {
    --bg: #e9e9e6;
    --card: #ffffff;
    --slate: #4f6a6a;
    --slate-light: #869a9a;
    --olive: #7d9a48;
    --rule: #c2b9a8;
    --badge-fill: #dcdcd8;
    --badge-ring: #ecebe6;
  }
  * { box-sizing: border-box; margin: 0; padding: 0; }
  html, body {
    width: 1200px; height: 1200px; overflow: hidden;
    background: var(--bg);
    font-family: "Merriweather", Georgia, serif;
  }
  .card {
    position: absolute; left: 100px; top: 314px;
    width: 1000px; height: 572px;
    background: var(--card);
    box-shadow: 0 10px 30px rgba(0,0,0,.12);
  }
  .brand {
    position: absolute; left: 60px; top: 118px; width: 330px;
    display: flex; align-items: center; gap: 14px;
  }
  .brand-dot {
    flex: none; width: 22px; height: 22px; border-radius: 50%;
    background: var(--slate);
  }
  .brand-name {
    font-weight: 900; font-size: 30px; line-height: 1.12;
    color: var(--slate); text-transform: uppercase; letter-spacing: .5px;
  }
  .brand-rule {
    position: absolute; left: 60px; top: 222px; width: 330px; height: 2px;
    background: var(--rule);
  }
  .usa-badge {
    position: absolute; left: 80px; top: 292px; width: 150px; height: 150px;
    border-radius: 50%;
    border: 6px solid var(--badge-ring);
    background: var(--badge-fill);
  }
  .person {
    position: absolute; left: 450px; top: 92px; right: 30px;
  }
  .person-name {
    font-weight: 700; font-size: 44px; color: var(--slate);
    text-transform: uppercase; letter-spacing: 1px; line-height: 1.1;
    white-space: nowrap;
  }
  .person-title, .person-company {
    font-weight: 700; font-size: 28px; color: var(--olive); line-height: 1.2;
  }
  .person-title { margin-top: 14px; }
  .contact {
    position: absolute; left: 450px; top: 290px; list-style: none;
  }
  .contact li {
    display: flex; align-items: center; gap: 20px;
    font-size: 18px; color: var(--slate); height: 46px;
  }
  .contact li.address { align-items: flex-start; height: auto; line-height: 1.4; margin-top: 6px; }
  .icon {
    flex: none; width: 34px; height: 34px; border-radius: 50%;
    background: var(--slate-light);
    display: flex; align-items: center; justify-content: center;
  }
  .bottom-rule {
    position: absolute; left: 430px; top: 512px; width: 520px; height: 5px;
    background: linear-gradient(90deg, var(--slate-light), var(--slate));
  }
</style>
</head>
<body>
  <main class="card">
    <div class="brand">
      <span class="brand-dot"></span>
      <span class="brand-name">Hollow Creek<br>Pet Works</span>
    </div>
    <div class="brand-rule"></div>
    <div class="usa-badge" role="img" aria-label="Made in the USA emblem"></div>

    <section class="person">
      <h1 class="person-name">Tom Willoughby</h1>
      <p class="person-title">CEO</p>
      <p class="person-company">Hollow Creek Pet Works</p>
    </section>

    <ul class="contact">
      <li><span class="icon"><svg width="18" height="18" viewBox="0 0 24 24"><path fill="#fff" d="M6.6 10.8a15 15 0 0 0 6.6 6.6l2.2-2.2a1 1 0 0 1 1-.25 11.4 11.4 0 0 0 3.6.57 1 1 0 0 1 1 1V20a1 1 0 0 1-1 1A17 17 0 0 1 3 4a1 1 0 0 1 1-1h3.5a1 1 0 0 1 1 1c0 1.25.2 2.450.57 3.6a1 1 0 0 1-.25 1z"/></svg></span>office: 314.555.0182</li>
      <li><span class="icon"><svg width="18" height="18" viewBox="0 0 24 24"><path fill="#fff" d="M6.6 10.8a15 15 0 0 0 6.6 6.6l2.2-2.2a1 1 0 0 1 1-.25 11.4 11.4 0 0 0 3.6.57 1 1 0 0 1 1 1V20a1 1 0 0 1-1 1A17 17 0 0 1 3 4a1 1 0 0 1 1-1h3.5a1 1 0 0 1 1 1c0 1.25.2 2.45.57 3.6a1 1 0 0 1-.25 1z"/></svg></span>mobile: 770.555.0139</li>
      <li><span class="icon"><svg width="18" height="18" viewBox="0 0 24 24"><path fill="none" stroke="#fff" stroke-width="2.4" d="M4 7l8 7 8-7"/></svg></span>email: tom@hollowcreekpetworks.com</li>
      <li class="address"><span class="icon"><svg width="16" height="18" viewBox="0 0 24 24"><path fill="#fff" d="M12 2a7 7 0 0 0-7 7c0 5 7 13 7 13s7-8 7-13a7 7 0 0 0-7-7zm0 9.5A2.5 2.5 0 1 1 12 6.5a2.5 2.5 0 0 1 0 5z"/></svg></span><span>5817 Brookhaven Commerce Lane<br>St. Louis, MO 63521</span></li>
    </ul>

    <div class="bottom-rule"></div>
  </main>
</body>
</html>
```